Washing Up Liquid Label

We are looking for 2 labels to be designed to be part of a range of products.

The brand is Marlow Brite and we are looking for a label design to you on washing up liquid bottle similar to the ones in the file attached.

One label it be original and the liquid will be green so the label colour needs to be green or work with the green. The other label is lemon and is yellow.

Please see attached the Marlow Brite logo and also a couple of the other designs in the range.

```html
<!DOCTYPE html>
<html lang="en">
<head>
<meta charset="utf-8">
<title>Marlow Brite Original – Washing Up Liquid Label</title>
<link rel="stylesheet" href="https://fonts.googleapis.com/css2?family=Open+Sans:ital,wght@0,700;0,800;1,800&display=swap">
<style>
  :root {
    --backdrop-light: #f6f6f6;
    --backdrop-dark: #dedede;
    --label-green: #6fd14f;
    --label-green-deep: #3fae2a;
    --label-mist: #f4fbf0;
    --brand-blue: #1b5fc4;
    --title-light: #f3fbe9;
    --title-green: #5cbf2e;
    --title-shadow: #2f7a12;
    --copy-green: #2e6a0e;
    --volume-green: #2f5b0c;
  }
  * { margin: 0; padding: 0; box-sizing: border-box; }
  html, body {
    width: 1200px;
    height: 857px;
    overflow: hidden;
  }
  body {
    position: relative;
    background: radial-gradient(ellipse at 50% 45%, var(--backdrop-light) 0%, var(--backdrop-dark) 100%);
    font-family: "Open Sans", Arial, sans-serif;
  }
  .label {
    position: absolute;
    left: 203px;
    top: 30px;
    width: 794px;
    height: 794px;
    border-radius: 50%;
    filter: drop-shadow(0 2px 6px rgba(0,0,0,0.12));
  }
  .label-art { position: absolute; inset: 0; }
  .brand-name {
    position: absolute;
    left: 0;
    right: 0;
    top: 205px;
    text-align: center;
    font-weight: 800;
    font-size: 100px;
    letter-spacing: -1px;
    color: var(--brand-blue);
  }
  .variant-title {
    position: absolute;
    left: 0;
    right: 0;
    top: 438px;
    text-align: center;
    font-weight: 800;
    font-style: italic;
    font-size: 78px;
    letter-spacing: 1px;
    background: linear-gradient(180deg, var(--title-light) 20%, var(--title-green) 95%);
    -webkit-background-clip: text;
    background-clip: text;
    color: transparent;
    filter: drop-shadow(3px 4px 2px var(--title-shadow));
  }
  .product-copy {
    position: absolute;
    left: 296px;
    width: 610px;
    top: 576px;
    font-weight: 700;
    font-size: 15.5px;
    line-height: 23.5px;
    color: var(--copy-green);
    text-align: justify;
    text-align-last: center;
  }
  .volume {
    position: absolute;
    left: 0;
    right: 0;
    top: 720px;
    text-align: center;
    font-weight: 800;
    font-size: 50px;
    color: var(--volume-green);
  }
</style>
</head>
<body>
  <div class="label">
    <svg class="label-art" viewBox="0 0 794 794" width="794" height="794">
      <defs>
        <radialGradient id="labelFill" cx="0.55" cy="0.38" r="0.7">
          <stop offset="0" stop-color="#ffffff"/>
          <stop offset="0.35" stop-color="#e9f8e0"/>
          <stop offset="0.75" stop-color="#8fdc6c"/>
          <stop offset="1" stop-color="#5cc93a"/>
        </radialGradient>
        <linearGradient id="sweep" x1="0" y1="0" x2="1" y2="1">
          <stop offset="0" stop-color="#4fbf2c" stop-opacity="0.7"/>
          <stop offset="1" stop-color="#9ee67c" stop-opacity="0.2"/>
        </linearGradient>
        <clipPath id="labelClip"><circle cx="397" cy="397" r="397"/></clipPath>
      </defs>
      <circle cx="397" cy="397" r="397" fill="url(#labelFill)"/>
      <g clip-path="url(#labelClip)">
        <path d="M0 330 C120 360 170 470 260 540 C340 600 470 610 560 560 C420 640 250 620 160 520 C90 440 40 390 0 380 Z" fill="url(#sweep)"/>
        <path d="M0 620 C180 700 420 740 794 650 L794 794 L0 794 Z" fill="#62cd40" opacity="0.55"/>
        <path d="M60 680 C260 760 520 760 794 700" fill="none" stroke="#ffffff" stroke-width="6" opacity="0.45"/>
        <path d="M794 120 C700 200 640 260 600 340" fill="none" stroke="#ffffff" stroke-width="10" opacity="0.35"/>
      </g>
    </svg>
  </div>

  <div class="brand-name">Marlow Brite</div>
  <div class="variant-title">ORIGINAL</div>
  <p class="product-copy">Lorem ipsum dolor sit amet, consectetur adipisicing elit, sed do eiusmod tempor incididunt ut labore et dolore magna aliqua. Ut enim ad minim veniam, quis nostrud exercitation. Lorem ipsum dolor sit amet, consectetur adipisicing elit, sed do eiusmod tempor incididunt ut labore et dolore magna aliqua.</p>
  <div class="volume">50mL</div>
</body>
</html>
```